Upscale business cards needed for Board of Directors

We need professional business cards created for members of our family business Board of Directors. We would like these relatively simple and straightforward, but also with a unique element to set them apart. Probably stick with neutral and simple colors - white, grey etc. We need space for the traditional elements, including name, title, address, email/phone number. And we will be creating several from this template so it needs to be template that is easy to switch information in and out of.
Business
See description

```html
<!DOCTYPE html>
<html lang="en">
<head>
<meta charset="utf-8">
<title>Harborline Holdings – Business Card</title>
<link rel="stylesheet" href="https://fonts.googleapis.com/css2?family=Poppins:wght@400;500;700&display=swap">
<style>
  :root {
    --backdrop: #e9e7e3;
    --card: #fbfbfa;
    --ink: #1f1f1f;
    --gold: #b5a27c;
    --gold-deep: #9c8a63;
  }
  html, body {
    margin: 0;
    width: 1200px;
    height: 1022px;
    overflow: hidden;
    background: var(--backdrop);
    font-family: "Poppins", sans-serif;
  }
  .card {
    position: absolute;
    left: 150px;
    top: 254px;
    width: 900px;
    height: 514px;
    background: var(--card);
    border-radius: 14px;
    box-shadow: 0 10px 30px rgba(0,0,0,0.12);
    overflow: hidden;
  }
  .card-art {
    position: absolute;
    inset: 0;
  }
  .brand {
    position: absolute;
    left: 64px;
    top: 300px;
    display: flex;
    align-items: center;
    gap: 12px;
    color: var(--ink);
    font-size: 29px;
    font-weight: 700;
    line-height: 1;
    white-space: nowrap;
  }
  .brand-mark {
    width: 14px;
    height: 14px;
    background: var(--ink);
    flex: none;
  }
  .details {
    position: absolute;
    left: 472px;
    top: 112px;
    color: var(--ink);
  }
  .person-name {
    margin: 0;
    font-size: 34px;
    font-weight: 500;
    color: var(--gold);
    line-height: 1.1;
  }
  .person-title {
    margin: 4px 0 0;
    font-size: 18px;
  }
  .address {
    margin: 26px 0 0;
    font-size: 20px;
    font-style: normal;
    line-height: 1.5;
  }
  .contact {
    list-style: none;
    margin: 18px 0 0;
    padding: 0;
    font-size: 20px;
    line-height: 1.6;
  }
  .contact li {
    display: flex;
    align-items: center;
    gap: 12px;
  }
  .contact svg { width: 16px; height: 16px; flex: none; }
  .domain { color: var(--gold); font-weight: 700; }
</style>
</head>
<body>
  <article class="card">
    <svg class="card-art" viewBox="0 0 900 514" aria-hidden="true">
      <defs>
        <linearGradient id="divider-fade" x1="0" y1="0" x2="0" y2="1">
          <stop offset="0" stop-color="#1f1f1f" stop-opacity="0"/>
          <stop offset="0.5" stop-color="#1f1f1f" stop-opacity="1"/>
          <stop offset="1" stop-color="#1f1f1f" stop-opacity="0"/>
        </linearGradient>
      </defs>
      <line class="column-divider" x1="432" y1="130" x2="446" y2="360" stroke="url(#divider-fade)" stroke-width="2"/>
      <polygon class="edge-band" points="0,498 300,498 312,486 340,486 340,514 0,514" fill="var(--gold)"/>
      <polygon class="edge-band" points="580,486 598,486 610,498 900,498 900,514 580,514" fill="var(--gold)"/>
      <rect x="0" y="510" width="900" height="4" fill="var(--gold-deep)" opacity="0.35"/>
    </svg>

    <div class="brand">
      <span class="brand-mark"></span>
      <span class="brand-name">Harborline Holdings</span>
    </div>

    <section class="details">
      <h1 class="person-name">Marcus Ellery</h1>
      <p class="person-title">Director</p>
      <address class="address">2580 Linden Park Ave.<br>Fairview CA 90000</address>
      <ul class="contact">
        <li>
          <svg viewBox="0 0 16 16"><path d="M4 1.5l2.5 3-1.5 1.6c.8 1.8 2.2 3.2 4 4l1.6-1.5 3 2.5-1.6 2.4C7.5 13.3 2.7 8.5 1.5 3.1z" fill="none" stroke="var(--gold)" stroke-width="1.3"/></svg>
          +100 5550-1234
        </li>
        <li>
          <svg viewBox="0 0 16 16"><rect x="1.5" y="3.5" width="13" height="9" fill="none" stroke="var(--gold)" stroke-width="1.3"/><path d="M1.5 3.5l6.5 5 6.5-5" fill="none" stroke="var(--gold)" stroke-width="1.3"/></svg>
          info@harborlineholdings.com
        </li>
        <li>
          <svg viewBox="0 0 16 16"><circle cx="8" cy="8" r="6.5" fill="none" stroke="var(--gold)" stroke-width="1.3"/><ellipse cx="8" cy="8" rx="3" ry="6.5" fill="none" stroke="var(--gold)" stroke-width="1.1"/><path d="M1.5 8h13M2.5 5h11M2.5 11h11" stroke="var(--gold)" stroke-width="1"/></svg>
          <span>www.<span class="domain">harborlineholdings</span>.com</span>
        </li>
      </ul>
    </section>
  </article>
</body>
</html>
```